New business card design needed for Diesel Fitting (Mechanical) Company

We need a new business card for our company called "Gumtree Engine Works" that showcases our logo and business details.
Target Market(s)
Owners of all makes and models of vehicles, trucks, plant and machinery.
Industry/Entity Type
Mechanical
Contact Information for Business Card
The business card details need to include the following: Owners/Directors: Doug & Marisol Brent-Coyle ABN: 41 917 302 846 Address: 317 Wattlebrook Street CHARTERS TOWERS QLD 4820 Postal Address: PO Box 5791 CHARTERS TOWERS QLD 4820 Website: www.gewservice.com.au Phone: 4712 9083 Mobile: 0438 175 906 Emails: sales@gewservice.com.au; admin@gewservice.com.au; accounts@gewservice.com.au; parts@gewservice.com.au; office@gewservice.com.au, reception@gewservice.com.au
Look and feel

```html
<!DOCTYPE html>
<html lang="en">
<head>
<meta charset="utf-8">
<title>Gumtree Engine Works – Business Card</title>
<link rel="stylesheet" href="https://fonts.googleapis.com/css2?family=Montserrat:wght@600;700;800&family=Questrial&display=swap">
<style>
  :root {
    --navy: #021641;
    --orange: #ff5008;
    --orange-soft: rgba(255, 80, 8, 0.38);
    --orange-fade: rgba(255, 80, 8, 0);
    --white: #ffffff;
    --ink: #0a0a0a;
  }
  * { margin: 0; padding: 0; box-sizing: border-box; }
  html, body { width: 927px; height: 1200px; overflow: hidden; background: var(--navy); }
  .sheet { position: relative; width: 927px; height: 1200px; background: var(--navy); }
  .card { position: absolute; left: 36px; width: 869px; background: var(--white); overflow: hidden; }
  .card--front { top: 49px; height: 497px; }
  .card--back { top: 630px; height: 497px; }

  /* front */
  .dot-field { position: absolute; top: 0; height: 100%; }
  .dot-field--left { left: 0; width: 135px;
    background: linear-gradient(90deg, var(--orange-soft) 0%, rgba(255,80,8,0.22) 55%, var(--orange-fade) 100%); }
  .dot-field--right { right: 0; width: 120px;
    background: linear-gradient(270deg, var(--orange-soft) 0%, rgba(255,80,8,0.22) 55%, var(--orange-fade) 100%); }

  .brand { position: absolute; display: flex; align-items: center;
    font-family: "Montserrat", sans-serif; font-weight: 800; color: var(--orange); white-space: nowrap; }
  .brand__mark { border-radius: 50%; background: var(--orange); flex: none; }
  .brand--front { left: 0; right: 0; top: 150px; height: 110px; justify-content: center; gap: 22px; font-size: 42px; }
  .brand--front .brand__mark { width: 104px; height: 104px; }

  .web-rule { position: absolute; left: 20px; right: 20px; top: 449px; height: 1px;
    background: linear-gradient(90deg, var(--orange-fade) 0%, var(--orange) 30%, var(--orange) 70%, var(--orange-fade) 100%); }
  .web-pill { position: absolute; left: 285px; top: 433px; width: 301px; height: 32px;
    border: 1.5px solid var(--orange); border-radius: 7px; background: var(--white);
    font-family: "Montserrat", sans-serif; font-weight: 700; font-size: 20px; color: var(--orange);
    display: flex; align-items: center; justify-content: center; letter-spacing: 0.3px; }

  /* back */
  .brand--back { left: 40px; width: 360px; top: 48px; flex-direction: column; gap: 16px; font-size: 27px; line-height: 1.1; }
  .brand--back .brand__mark { width: 118px; height: 118px; }
  .abn { position: absolute; left: 40px; width: 360px; top: 232px; text-align: center;
    font-family: "Questrial", sans-serif; font-size: 19px; color: var(--ink); }
  .abn__number { color: var(--orange); }

  .band { position: absolute; background: var(--orange); }
  .band--slanted { right: 0; width: 371px; height: 92px; clip-path: polygon(55px 0, 100% 0, 100% 100%, 0 100%); }
  .band--directors { top: 36px; }
  .band--contacts { top: 172px; }
  .band--emails { left: 0; right: 0; top: 305px; height: 91px; }
  .band--address { left: 0; right: 0; top: 405px; height: 92px; }

  .label-pill { position: absolute; height: 36px; border: 1.5px solid var(--orange); border-radius: 7px;
    background: var(--white); box-shadow: 1px 1px 2px rgba(0,0,0,0.25);
    font-family: "Montserrat", sans-serif; font-weight: 700; font-size: 19px; color: var(--orange);
    display: flex; align-items: center; justify-content: center; letter-spacing: 0.4px; }
  .label-pill--directors { left: 452px; top: 63px; width: 136px; }
  .label-pill--contacts { left: 452px; top: 199px; width: 136px; }
  .label-pill--emails { left: 366px; top: 284px; width: 136px; height: 34px; }
  .label-pill--address { left: 366px; top: 386px; width: 136px; height: 34px; }

  .directors { position: absolute; left: 590px; width: 264px; top: 46px; text-align: center;
    font-family: "Montserrat", sans-serif; font-weight: 700; font-size: 22px; color: var(--white); line-height: 35px; }
  .contacts { position: absolute; left: 608px; top: 178px; font-family: "Montserrat", sans-serif; font-weight: 700;
    font-size: 24px; color: var(--white); }
  .contacts__row { display: flex; align-items: center; height: 39px; }
  .contacts__icon { width: 28px; height: 28px; margin-right: 18px; flex: none; }

  .emails { position: absolute; left: 0; right: 0; top: 312px; height: 78px;
    font-family: "Questrial", sans-serif; font-size: 18.5px; color: var(--white); }
  .emails__item { position: absolute; transform: translateX(-50%); white-space: nowrap; }

  .address { position: absolute; top: 418px; display: flex; align-items: center;
    font-family: "Questrial", sans-serif; font-size: 19.5px; line-height: 20px; color: var(--white); letter-spacing: 0.5px; }
  .address--street { left: 32px; }
  .address--postal { left: 560px; }
  .address__icon { flex: none; margin-right: 8px; }
</style>
</head>
<body>
<main class="sheet">

  <section class="card card--front" aria-label="Card front">
    <div class="dot-field dot-field--left" role="img" aria-label="Decorative orange dots and swoosh along the left edge"></div>
    <div class="dot-field dot-field--right" role="img" aria-label="Decorative orange dots and swoosh along the right edge"></div>
    <div class="brand brand--front"><span class="brand__mark"></span>Gumtree Engine Works</div>
    <div class="web-rule"></div>
    <div class="web-pill">www.gewservice.com.au</div>
  </section>

  <section class="card card--back" aria-label="Card back">
    <div class="brand brand--back"><span class="brand__mark"></span>Gumtree Engine Works</div>
    <p class="abn">ABN: <span class="abn__number">41 917 302 846</span></p>

    <div class="band band--slanted band--directors"></div>
    <div class="label-pill label-pill--directors">DIRECTORS</div>
    <div class="directors">
      <p>Doug Brent-Coyle</p>
      <p>Marisol Brent-Coyle</p>
    </div>

    <div class="band band--slanted band--contacts"></div>
    <div class="label-pill label-pill--contacts">CONTACTS</div>
    <div class="contacts">
      <p class="contacts__row">
        <svg class="contacts__icon" viewBox="0 0 28 28" aria-hidden="true">
          <path d="M2 10 C 6 3, 22 3, 26 10 L 21 12 L 19 8 C 16 7, 12 7, 9 8 L 7 12 Z" fill="var(--white)"/>
          <path d="M8 13 L 20 13 L 25 24 L 3 24 Z" fill="var(--white)"/>
          <circle cx="14" cy="18.5" r="3" fill="var(--orange)"/>
        </svg>4712 9083
      </p>
      <p class="contacts__row">
        <svg class="contacts__icon" viewBox="0 0 28 28" aria-hidden="true">
          <rect x="7" y="1" width="14" height="26" rx="2.5" fill="none" stroke="var(--white)" stroke-width="2.4"/>
          <circle cx="14" cy="23" r="1.5" fill="var(--white)"/>
        </svg>0438 175 906
      </p>
    </div>

    <div class="band band--emails"></div>
    <div class="label-pill label-pill--emails">EMAILS</div>
    <div class="emails">
      <span class="emails__item" style="left:155px;top:0">admin@gewservice.com.au</span>
      <span class="emails__item" style="left:155px;top:47px">office@gewservice.com.au</span>
      <span class="emails__item" style="left:423px;top:7px">sales@gewservice.com.au</span>
      <span class="emails__item" style="left:423px;top:41px">parts@gewservice.com.au</span>
      <span class="emails__item" style="left:697px;top:0">reception@gewservice.com.au</span>
      <span class="emails__item" style="left:697px;top:47px">accounts@gewservice.com.au</span>
    </div>

    <div class="band band--address"></div>
    <div class="label-pill label-pill--address">ADDRESS</div>
    <p class="address address--street">
      <svg class="address__icon" width="30" height="38" viewBox="0 0 30 38" aria-hidden="true">
        <path d="M15 36 C 8 27, 2 20, 2 14 A 13 13 0 0 1 28 14 C 28 20, 22 27, 15 36 Z" fill="none" stroke="var(--white)" stroke-width="2.6"/>
        <circle cx="15" cy="14" r="5" fill="none" stroke="var(--white)" stroke-width="2.6"/>
      </svg>
      <span>317 Wattlebrook Street, Charters<br>Towers, QLD 4820.</span>
    </p>
    <p class="address address--postal">
      <svg class="address__icon" width="38" height="30" viewBox="0 0 38 30" aria-hidden="true">
        <rect x="2" y="2" width="34" height="26" rx="4" fill="none" stroke="var(--white)" stroke-width="2.6"/>
        <path d="M3 4 L 19 17 L 35 4" fill="none" stroke="var(--white)" stroke-width="2.6"/>
      </svg>
      <span>PO Box 5791, Charters<br>Towers, QLD 4820.</span>
    </p>
  </section>

</main>
</body>
</html>
```